Agriculture Security Company needs a business card design

We need a business card design for a new company based in Seattle calls Corvantel Guard LLC. We provide high-end physical security solutions that is geared and focused towards to the marijuana grow operations, wholesalers and distributors. We DO NOT get involved in the retail operations (store fronts). We would like to see designs that incorporate professionalism, reliability, trustworthy and forward thinking as traits of our organization.

Industry/Entity Type

Security

```html
<!DOCTYPE html>
<html lang="en">
<head>
<meta charset="utf-8">
<title>Corvantel Guard LLC – Business Card</title>
<link rel="stylesheet" href="https://fonts.googleapis.com/css2?family=Arimo:wght@400;700&display=swap">
<style>
  :root {
    --green-dark: #0f7a35;
    --green-light: #7cb82f;
    --grey-text: #4d4d4d;
    --card: #ffffff;
    --backdrop: #a8672a;
  }
  * { margin: 0; padding: 0; box-sizing: border-box; }
  html, body { width: 1080px; height: 1200px; overflow: hidden; }
  body {
    position: relative;
    background: var(--backdrop);
    font-family: "Arimo", Arial, sans-serif;
  }
  .card {
    position: absolute;
    left: 128px;
    width: 840px;
    height: 479px;
    background: var(--card);
  }
  .card-front { top: 78px; }
  .card-back { top: 634px; }

  .brand-name {
    position: absolute;
    display: flex;
    align-items: center;
    gap: 12px;
    font-family: "Arimo", Arial, sans-serif;
    font-weight: 700;
    color: var(--green-dark);
    white-space: nowrap;
    line-height: 1;
  }
  .brand-dot {
    flex: none;
    border-radius: 50%;
    background: var(--green-light);
  }
  .card-front .brand-name { left: 51px; top: 92px; font-size: 31px; }
  .card-front .brand-dot { width: 16px; height: 16px; }

  .name-rule {
    position: absolute;
    top: 218px;
    height: 4px;
    background: var(--green-dark);
  }
  .name-rule.left { left: 0; width: 62px; }
  .name-rule.right { left: 378px; right: 0; }
  .person {
    position: absolute;
    left: 70px;
    top: 206px;
    width: 296px;
    color: var(--grey-text);
  }
  .person-name { font-size: 19px; text-align: center; letter-spacing: .5px; }
  .person-role { font-size: 16px; text-align: right; margin-top: 2px; }

  .address {
    position: absolute;
    left: 80px;
    top: 280px;
    font-size: 16px;
    color: var(--grey-text);
    letter-spacing: .3px;
  }
  .contact {
    position: absolute;
    display: flex;
    align-items: center;
    gap: 22px;
    font-size: 19px;
    color: var(--grey-text);
    letter-spacing: .3px;
  }
  .contact svg { width: 38px; height: 38px; flex: none; }
  .contact.mobile { left: 70px; top: 318px; }
  .contact.phone  { left: 70px; top: 370px; }
  .contact.web    { left: 474px; top: 318px; }
  .contact.email  { left: 474px; top: 370px; }

  .base-rule {
    position: absolute;
    left: 0; right: 0;
    top: 442px;
    height: 5px;
    background: var(--green-dark);
  }
  .base-band {
    position: absolute;
    left: 0; right: 0;
    top: 455px;
    bottom: 0;
    background: linear-gradient(90deg, #6aa92a, var(--green-light) 60%, #8cc63f);
  }

  .frame { position: absolute; }
  .frame-outer { inset: 5px; border: 4px solid var(--green-light); }
  .frame-main  { left: 21px; top: 24px; right: 27px; bottom: 24px; border: 8px solid var(--green-dark); }
  .frame-inner { left: 33px; top: 36px; right: 39px; bottom: 36px; border: 3px solid var(--green-light); }

  .card-back .brand-name {
    left: 0; right: 0;
    top: 214px;
    justify-content: center;
    font-size: 50px;
    gap: 16px;
  }
  .card-back .brand-dot { width: 24px; height: 24px; }
</style>
</head>
<body>
  <section class="card card-front">
    <div class="brand-name"><span class="brand-dot"></span>Corvantel Guard LLC</div>

    <div class="name-rule left"></div>
    <div class="name-rule right"></div>
    <div class="person">
      <p class="person-name">XXXXXX-NAME-XXXXXXX</p>
      <p class="person-role">DESIGNATION</p>
    </div>

    <p class="address">XXADDRESSXX, XXXXXXXXXXXXXXXXXX, XXXXXXXXXXXXX</p>

    <div class="contact mobile">
      <svg viewBox="0 0 40 40" aria-hidden="true">
        <circle cx="20" cy="20" r="19" fill="#7cb82f"/><circle cx="20" cy="20" r="15.5" fill="none" stroke="#fff" stroke-width="1.2"/>
        <rect x="15" y="10" width="10" height="20" rx="2" fill="none" stroke="#fff" stroke-width="2"/>
        <circle cx="20" cy="26.5" r="1.2" fill="#fff"/>
      </svg>
      <span>XXXXXXXXXXXXXXXXX</span>
    </div>
    <div class="contact phone">
      <svg viewBox="0 0 40 40" aria-hidden="true">
        <circle cx="20" cy="20" r="19" fill="#7cb82f"/><circle cx="20" cy="20" r="15.5" fill="none" stroke="#fff" stroke-width="1.2"/>
        <path d="M14 11c1.5-1 3-.5 3.6.8l1.4 3c.4 1-.1 1.9-1 2.5l-.8.6c.8 2 2.3 3.6 4.3 4.5l.6-.8c.6-.9 1.6-1.3 2.5-.9l3 1.4c1.3.6 1.7 2.1.8 3.6-1 1.6-3 2.4-5 1.7-5.1-1.8-8.8-5.5-10.5-10.6-.6-2 .2-4 1.1-5.8z" fill="#fff"/>
      </svg>
      <span>XXXXXXXXXXXXXXXXX</span>
    </div>
    <div class="contact web">
      <svg viewBox="0 0 40 40" aria-hidden="true">
        <circle cx="20" cy="20" r="19" fill="#7cb82f"/><circle cx="20" cy="20" r="15.5" fill="none" stroke="#fff" stroke-width="1.2"/>
        <g fill="none" stroke="#fff" stroke-width="1.6">
          <circle cx="20" cy="20" r="9"/><ellipse cx="20" cy="20" rx="4" ry="9"/>
          <path d="M11 20h18M12.5 15h15M12.5 25h15"/>
        </g>
      </svg>
      <span>XXXXXXXXXXXXXXXXX</span>
    </div>
    <div class="contact email">
      <svg viewBox="0 0 40 40" aria-hidden="true">
        <circle cx="20" cy="20" r="19" fill="#7cb82f"/><circle cx="20" cy="20" r="15.5" fill="none" stroke="#fff" stroke-width="1.2"/>
        <rect x="11" y="14" width="18" height="12" fill="#fff"/>
        <path d="M11 14l9 7 9-7" fill="none" stroke="#7cb82f" stroke-width="1.5"/>
      </svg>
      <span>XXXXXXXXXXXXXXXXX</span>
    </div>

    <div class="base-rule"></div>
    <div class="base-band"></div>
  </section>

  <section class="card card-back">
    <div class="frame frame-outer"></div>
    <div class="frame frame-main"></div>
    <div class="frame frame-inner"></div>
    <div class="brand-name"><span class="brand-dot"></span>Corvantel Guard LLC</div>
  </section>
</body>
</html>
```